11X17 Vorumbax Sports Performance Program Poster

We need a poster done for our Sports Performance Program 11x17 with room for bleed. Here a website of our program to help with the design and some sales copy: http://www.dolprevato.com.
Info about the program needed for the poster:
Vorumbax's Sports Performance program starts Monday June 1st 2015 and runs through Friday July 31st.
Ages 12-18
For Serious Athletes Only!
We have two time options: Monday, Wednesday and Fridays at 10:30-11:30am or 3:30-4:30pm. Athletes must stay on their time track chosen.
$99 per month or $179 for both months.
Somewhere at the bottom of the poster please put "Powered By:" and add the Vorumbax Personal Training logo provided.
We need the poster in editable PSD format (CS3 compatible please).

```html
<!DOCTYPE html>
<html lang="en">
<head>
<meta charset="utf-8">
<title>Vorumbax's Sports Performance Program</title>
<link href="https://fonts.googleapis.com/css2?family=Questrial&family=Open+Sans:ital,wght@1,700&display=swap" rel="stylesheet">
<style>
  :root {
    --black: #000000;
    --white: #ffffff;
    --grey: #8a8a8a;
    --orange: #f7941d;
    --red: #ed1c24;
    --tag-red: #e8262c;
    --photo-top: #0d0f12;
    --photo-mid: #2a2d2a;
    --photo-accent: #4f5a1f;
  }
  html, body {
    margin: 0;
    padding: 0;
    overflow: hidden;
    background: var(--black);
  }
  .poster {
    position: relative;
    width: 776px;
    height: 1200px;
    overflow: hidden;
    background: var(--black);
    font-family: "Questrial", "Century Gothic", sans-serif;
    color: var(--white);
  }
  .hero-photo {
    position: absolute;
    left: 0;
    top: 480px;
    width: 776px;
    height: 720px;
    background:
      radial-gradient(ellipse 190px 230px at 200px 260px, var(--photo-accent) 0%, rgba(79,90,31,0.35) 45%, transparent 75%),
      radial-gradient(ellipse 260px 380px at 190px 420px, var(--photo-mid) 0%, transparent 80%),
      linear-gradient(180deg, var(--black) 0%, var(--photo-top) 20%, #1b1c1d 60%, #0a0a0a 100%);
  }
  .title {
    position: absolute;
    left: 0;
    width: 776px;
    text-align: center;
    margin: 0;
    font-weight: 400;
    line-height: 1;
  }
  .title-main { top: 12px; font-size: 66px; letter-spacing: 0.5px; }
  .title-sub { top: 100px; font-size: 38px; letter-spacing: 0.5px; }
  .dates {
    position: absolute;
    top: 152px;
    left: 0;
    width: 776px;
    text-align: center;
    font-size: 20px;
    color: var(--grey);
    margin: 0;
  }
  .info-bands {
    position: absolute;
    top: 249px;
    left: 0;
    width: 776px;
    margin: 0;
    padding: 0;
    list-style: none;
  }
  .info-band {
    background: var(--orange);
    color: var(--black);
    text-align: center;
    font-size: 24px;
    line-height: 42px;
    margin-bottom: 6px;
  }
  .info-band.double { line-height: 42px; padding: 2px 0; }
  .tagline {
    position: absolute;
    top: 506px;
    left: 57px;
    margin: 0;
    font-family: "Open Sans", Arial, sans-serif;
    font-style: italic;
    font-weight: 700;
    font-size: 30px;
    letter-spacing: -0.5px;
  }
  .tagline .accent { color: var(--tag-red); }
  .price {
    position: absolute;
    width: 264px;
    height: 264px;
    border-radius: 50%;
    background: var(--red);
    text-align: center;
    color: var(--white);
  }
  .price-both { left: 448px; top: 558px; }
  .price-month { left: 457px; top: 868px; }
  .price-amount {
    display: block;
    font-family: "Open Sans", Arial, sans-serif;
    font-style: normal;
    font-weight: 700;
    font-size: 84px;
    line-height: 1;
    letter-spacing: -2px;
  }
  .price-both .price-amount { margin-top: 78px; }
  .price-month .price-amount { margin-top: 72px; }
  .price-note { display: block; font-size: 24px; line-height: 1.1; }
  .program-mark {
    position: absolute;
    left: 40px;
    top: 1030px;
    display: flex;
    align-items: center;
    gap: 18px;
  }
  .program-mark .dot {
    width: 70px;
    height: 70px;
    border-radius: 50%;
    background: var(--orange);
  }
  .program-mark .name {
    font-size: 34px;
    line-height: 1.05;
    color: var(--white);
  }
  .powered {
    position: absolute;
    left: 30px;
    top: 1128px;
    display: flex;
    align-items: baseline;
    gap: 22px;
  }
  .powered .label { font-size: 22px; }
  .powered .brand { font-size: 40px; letter-spacing: 1px; color: var(--white); }
</style>
</head>
<body>
  <main class="poster">
    <div class="hero-photo" role="img" aria-label="Sprinter in a green vest driving out of a starting crouch on a running track at dusk"></div>

    <h1 class="title title-main">VORUMBAX'S SPORTS</h1>
    <h2 class="title title-sub">PERFORMANCE PROGRAM</h2>
    <p class="dates">Monday June 1st 2015 and runs through Friday July 31st.</p>

    <ul class="info-bands">
      <li class="info-band">Ages 12-18</li>
      <li class="info-band">For Serious Athletes Only!</li>
      <li class="info-band double">We have two time options: Monday, Wednesday<br>and Fridays at 10:30-11:30am or 3:30-4:30pm.</li>
      <li class="info-band">Athletes must stay on their time track chosen.</li>
    </ul>

    <p class="tagline">Don’t just play Sport <span class="accent">excel at your game</span></p>

    <div class="price price-both">
      <span class="price-amount">$179</span>
      <span class="price-note">for both months.</span>
    </div>
    <div class="price price-month">
      <span class="price-amount">$99</span>
      <span class="price-note">per month</span>
    </div>

    <div class="program-mark">
      <span class="dot"></span>
      <span class="name">Dolprevato<br>Performance</span>
    </div>

    <div class="powered">
      <span class="label">Powered by</span>
      <span class="brand">VORUMBAX</span>
    </div>
  </main>
</body>
</html>
```